Postcard Design

I'm a licensed REALTORĀ® with Homestead Partners in East Tennessee specializing in residential real estate. I want to design a postcard that I can send to potential clients like for sale by owners and expired listings. I originally wanted to design 2 cards, but everything would be almost exact except for 1-2 sentences. I want to pinpoint my attributes and have a postcard that will catch client's eyes. I am applying my business logo and my profile picture. I am waiting on an updated photo from the photographer that I would prefer to use instead, but I also wanted to get started on this project.

Target Market(s)

For sale by owners and expired listings

Industry/Entity Type

Residential

Requirements
Must have
• I would like to point out why I would be a good candidate for these clients: Honesty and Integrity, Hard Working, Personal Attention to All Transactions, Extensive Market and Area Knowledge, Advertising and Marketing of the client's home.

```html
<!DOCTYPE html>
<html lang="en">
<head>
<meta charset="utf-8">
<title>Licensed Realtor Postcard</title>
<link href="https://fonts.googleapis.com/css2?family=Sorts+Mill+Goudy&display=swap" rel="stylesheet">
<style>
  :root {
    --navy: #2d3e51;
    --rust: #a2482b;
    --peach: #fde3cb;
    --white: #ffffff;
    --ink: #111111;
    --brand-red: #b4232f;
    --sky: #e4e9ef;
    --roof: #7d7f84;
    --wall: #d8d2c8;
    --shrub: #3c5526;
    --lawn: #6e8d3a;
  }
  html, body {
    margin: 0;
    padding: 0;
    width: 1200px;
    height: 923px;
    overflow: hidden;
    background: var(--white);
  }
  .postcard {
    position: relative;
    width: 1200px;
    height: 923px;
    font-family: "Sorts Mill Goudy", Georgia, serif;
    overflow: hidden;
  }
  .title-bar {
    position: absolute;
    left: 0; top: 0;
    width: 860px; height: 107px;
    background: var(--navy);
  }
  .title {
    margin: 0;
    position: absolute;
    left: 50px; top: 0;
    color: var(--white);
    font-weight: 400;
    font-size: 74px;
    line-height: 107px;
    white-space: nowrap;
  }
  .title sup { font-size: 28px; vertical-align: 34px; }
  .house-photo {
    position: absolute;
    left: 0; top: 107px;
    width: 438px; height: 637px;
    background:
      linear-gradient(180deg,
        var(--sky) 0%,
        #cfd5dc 14%,
        var(--roof) 24%,
        #9c9a96 30%,
        var(--wall) 38%,
        #c4bcae 50%,
        #8b8474 58%,
        var(--shrub) 66%,
        #4d6a2c 74%,
        var(--lawn) 84%,
        #5f7f32 100%);
  }
  .attributes {
    position: absolute;
    left: 438px; top: 107px;
    width: 422px; height: 637px;
    box-sizing: border-box;
    padding: 22px 6px 0 10px;
    background: var(--rust);
    color: var(--white);
    font-size: 30px;
    line-height: 46px;
  }
  .attributes p { margin: 0; }
  .attributes ul { list-style: none; margin: 0; padding: 0; }
  .attributes li::before { content: "\2022\00a0"; }
  .photo-slot {
    position: absolute;
    left: 860px; top: 0;
    width: 340px; height: 744px;
    box-sizing: border-box;
    background: var(--white);
    border-left: 8px solid var(--ink);
    border-bottom: 8px solid var(--ink);
  }
  .photo-slot span {
    position: absolute;
    left: 107px; top: 186px;
    font-size: 32px;
    line-height: 39px;
    color: var(--ink);
  }
  .contact-bar {
    position: absolute;
    left: 0; top: 744px;
    width: 1200px; height: 179px;
    background: var(--peach);
    color: var(--ink);
    font-size: 30px;
  }
  .brand {
    position: absolute;
    left: 54px; top: 62px;
    display: flex; align-items: center; gap: 10px;
    color: var(--brand-red);
    font-size: 26px;
    line-height: 1.1;
    width: 180px;
  }
  .brand-mark { width: 20px; height: 20px; background: var(--brand-red); flex: none; }
  .website { position: absolute; left: 296px; top: 82px; }
  .phone { position: absolute; left: 858px; top: 82px; }
</style>
</head>
<body>
  <div class="postcard">
    <header class="title-bar">
      <h1 class="title">Licensed Realtor<sup>®</sup></h1>
    </header>

    <div class="house-photo" role="img" aria-label="Photo of a two-story suburban home with grey roof, light siding, shrubs and a green front lawn"></div>

    <section class="attributes">
      <p>I'm a licensed REALTOR® with Homestead Partners in East Tennessee specializing in residential real estate.</p>
      <ul>
        <li>Honesty and Integrity</li>
        <li>Hard Working</li>
        <li>Personal Attention to All Transactions</li>
        <li>Extensive Market and Area Knowledge</li>
        <li>Advertising and Marketing of the client's home</li>
      </ul>
    </section>

    <aside class="photo-slot">
      <span>Your<br>Photo<br>Here</span>
    </aside>

    <footer class="contact-bar">
      <div class="brand"><span class="brand-mark"></span><span>Homestead Partners</span></div>
      <div class="website">Website</div>
      <div class="phone">Phone Number</div>
    </footer>
  </div>
</body>
</html>
```